KLD Rafter bench flyer for Vantor Machinery

Design a flyer that will be used on social media to promote our KLD Portal bench. This is to promote our tables to new market and under a new brand name. Design should we print the flyer to be on a 11x8.5 paper.
Included is the two accepted logo configuration of our brand - Vantor Machinery along with 2 photos of our latest installation. If you can change the logo on the installation from Pilsk Holdings to Vantor Machinery please.
Highlights of our machine to be included on flyer:
- Available in 12’ or 14’ wide
- Side or end eject
Highlights of our machine to add to flyer if your design can incorporate it:
- Heavy duty table top.
- T-slot opening for jigging
- All tables built to customers length requirements

For contact information to be put on flyer, Deshawn at (800)555-0192 or deshawn@pilskhold.example
Will have the website address added here as soon as it is done.

Please incorporate the following line (will prefer to have this at the bottom) : Vantor Machinery a brand manufactured by Pilsk Holdings Inc.

Our equipment colors are Clam white and Orange like seen on the equipment pictures.

Target Market(s)

Truss Manufacturers

Industry/Entity Type

Pre fabricated housing market and component manufacturers

Font styles to use
Sans Serif

Colors
EE7325
F08F49
F5BC92
FAE3D3
FDF4ED

Requirements
Must have
• a few highlights that are in the description
Nice to have
• Added to project description

```html
<!DOCTYPE html>
<html lang="en">
<head>
<meta charset="UTF-8">
<title>KLD Portal bench – Vantor Machinery flyer</title>
<link href="https://fonts.googleapis.com/css2?family=Open+Sans:wght@400;600;700&display=swap" rel="stylesheet">
<style>
  :root{
    --orange:#EE7325;
    --orange-mid:#F08F49;
    --orange-soft:#F5BC92;
    --orange-pale:#FAE3D3;
    --cream:#FDF4ED;
    --ink:#231f20;
    --paper:#ffffff;
    --stage:#e4e4e4;
  }
  *{margin:0;padding:0;box-sizing:border-box}
  html,body{width:900px;height:1200px;overflow:hidden}
  body{background:var(--stage);font-family:"Open Sans",Arial,sans-serif;color:var(--ink);position:relative}
  .flyer{position:absolute;left:70px;top:108px;width:760px;height:984px;background:var(--paper);overflow:hidden;box-shadow:0 4px 18px rgba(0,0,0,.18)}
  .flyer-backdrop{position:absolute;inset:0}
  .brand-lockup{position:absolute;font-weight:700;color:var(--ink);letter-spacing:1px;line-height:1}
  .brand-lockup--wide{left:86px;top:56px;font-size:29px;display:flex;align-items:center;gap:14px}
  .brand-lockup--wide .brand-square{width:26px;height:26px;background:var(--ink)}
  .brand-lockup--stacked{left:470px;top:44px;font-size:25px;text-align:center}
  .brand-lockup--stacked span{display:block}
  .hero-frame{position:absolute;left:110px;top:120px;width:538px;height:376px;background:var(--paper);padding:12px;box-shadow:0 3px 10px rgba(0,0,0,.35)}
  .photo{width:100%;height:100%}
  .photo--hero{background:linear-gradient(180deg,#4a3a2c 0%,#6b5a48 28%,#c9c6c0 45%,#e2ded6 70%,#a8a49c 100%)}
  .detail-frame{position:absolute;left:43px;top:524px;width:291px;height:248px;border:5px solid var(--ink);padding:8px;background:var(--paper)}
  .photo--detail{background:linear-gradient(180deg,#3e3126 0%,#7a6650 35%,#d9d5cc 60%,#b7b2a8 100%)}
  .product-title{position:absolute;left:380px;top:520px;width:400px;text-align:center;color:var(--orange);font-weight:700;line-height:1}
  .product-title__top{display:block;font-size:27px}
  .product-title__main{display:block;font-size:38px;margin-top:6px}
  .maker-line{position:absolute;left:330px;top:593px;width:420px;text-align:center;font-size:16px;font-weight:600}
  .feature-list{position:absolute;list-style:none;font-weight:600}
  .feature-list li{position:relative;padding-left:30px}
  .feature-list li::before{content:"";position:absolute;left:0;top:.38em;width:13px;height:13px;background:var(--orange)}
  .feature-list li.is-dark::before{background:var(--ink)}
  .feature-list--primary{left:402px;top:636px;font-size:20px;line-height:1.22}
  .feature-list--primary li{margin-bottom:14px}
  .feature-list--secondary{left:46px;top:798px;font-size:19px;line-height:1.6}
  .call-box{position:absolute;left:406px;top:794px;width:306px;height:38px;background:var(--orange);color:var(--paper);font-weight:700;font-size:23px;display:flex;align-items:center;justify-content:center}
  .mail-line{position:absolute;left:380px;top:842px;width:380px;text-align:center;font-size:18px}
  .site-address{position:absolute;left:0;top:932px;width:760px;text-align:center;color:var(--paper);font-size:13px;letter-spacing:3px}
</style>
</head>
<body>
  <main class="flyer">
    <svg class="flyer-backdrop" width="760" height="984" viewBox="0 0 760 984" aria-hidden="true">
      <polygon points="0,0 760,0 760,430 380,470 0,440" fill="#EE7325"/>
      <polygon points="0,250 110,210 110,250 0,290" fill="#F08F49"/>
      <polygon points="0,305 110,265 110,290 0,330" fill="#F5BC92" opacity=".7"/>
      <polygon points="0,345 110,305 110,330 0,370" fill="#F08F49"/>
      <polygon points="648,260 760,220 760,260 648,300" fill="#F08F49"/>
      <polygon points="648,315 760,275 760,300 648,340" fill="#F5BC92" opacity=".7"/>
      <polygon points="648,420 760,380 760,408 648,448" fill="#ffffff"/>
      <polygon points="648,448 760,408 760,430 648,470" fill="#231f20"/>
      <polygon points="0,400 110,440 110,496 0,470" fill="#231f20"/>
      <polygon points="60,984 370,876 700,984" fill="#231f20"/>
    </svg>

    <div class="brand-lockup brand-lockup--wide"><span class="brand-square"></span>VANTOR MACHINERY</div>
    <div class="brand-lockup brand-lockup--stacked"><span>VANTOR</span><span>MACHINERY</span></div>

    <div class="hero-frame">
      <div class="photo photo--hero" role="img" aria-label="Photo of the KLD Portal bench installed in a workshop, white gantry with orange work platform"></div>
    </div>

    <div class="detail-frame">
      <div class="photo photo--detail" role="img" aria-label="Photo of a long KLD bench table with orange ejection arm in a workshop"></div>
    </div>

    <h1 class="product-title">
      <span class="product-title__top">VANTOR</span>
      <span class="product-title__main">MACHINERY</span>
    </h1>
    <p class="maker-line">a brand manufactured by Pilsk Holdings Inc.</p>

    <ul class="feature-list feature-list--primary">
      <li>Heavy duty table top</li>
      <li class="is-dark">T-slot opening for jigging</li>
      <li>All tables built to customers<br>length requirements</li>
    </ul>

    <ul class="feature-list feature-list--secondary">
      <li>Available in 12’ or 14’ wide</li>
      <li>Side or end eject</li>
    </ul>

    <div class="call-box">CALL US- (800)555-0192</div>
    <p class="mail-line">mail us- deshawn@pilskhold.example</p>

    <p class="site-address">www.vantorsite.example</p>
  </main>
</body>
</html>
```